Apartments rental business needs a web for direct reservations.

I need a website that allows my clients to check the property (pictures, a brief description etc) and lets them make reservations. They will be providing the required information such as name, last name, email address and credit card details. Also a calendar where I can update the availability (dates and prices) of the property upon new reservations is a must. I already have a logo that should also be a good starting point for colors, style an inspiration.

Need extra days to review

```html
<!DOCTYPE html>
<html lang="en">
<head>
<meta charset="utf-8">
<title>The Orchard Bungalows</title>
<link href="https://fonts.googleapis.com/css2?family=Raleway:wght@400;600;700;800&family=Open+Sans:wght@400;600;700&family=Noto+Serif:wght@400;700&display=swap" rel="stylesheet">
<style>
:root{
  --orange:#f7941d;
  --orange-dark:#e5801a;
  --teal:#2bbcaa;
  --ink:#2b2b2b;
  --text:#555;
  --muted:#999;
  --line:#e3e3e3;
  --paper:#ffffff;
  --soft:#f4f4f4;
  --footer:#151515;
}
*{margin:0;padding:0;box-sizing:border-box}
html,body{width:1200px;height:3340px;overflow:hidden}
body{font-family:"Open Sans",Arial,sans-serif;color:var(--text);background:var(--paper);font-size:13px}
section,header,nav,footer{position:relative;width:1200px;overflow:hidden}
.abs{position:absolute}
h2.section-title{position:absolute;left:0;width:1200px;text-align:center;font-family:"Raleway",sans-serif;font-weight:700;font-size:30px;color:var(--ink);letter-spacing:.5px}
.divider{position:absolute;height:3px;width:100px;background:linear-gradient(90deg,transparent 0,transparent 10%,var(--orange) 10%,var(--orange) 45%,#f3c896 45%,#f3c896 90%,transparent 90%)}
.center-divider{left:550px}
.lead{position:absolute;text-align:center;font-size:14px;line-height:21px;color:var(--text)}
.btn{position:absolute;background:var(--orange);color:#fff;font-family:"Raleway",sans-serif;font-weight:700;font-size:14px;letter-spacing:.5px;display:flex;align-items:center;justify-content:center;text-transform:uppercase}

/* header */
.topbar{height:120px;background:#fff}
.brand{left:130px;top:38px;display:flex;align-items:center;gap:12px}
.brand-mark{width:40px;height:40px;border-radius:50%;background:var(--orange)}
.brand-name{font-family:"Raleway",sans-serif;font-weight:700;font-size:22px;color:var(--orange);letter-spacing:1px}
.contact-item{top:38px;display:flex;align-items:center;gap:14px}
.contact-item svg{width:38px;height:38px}
.contact-item small{display:block;font-size:12px;color:var(--muted)}
.contact-item strong{display:block;font-size:15px;color:var(--ink);font-weight:700}

.mainnav{height:47px;background:var(--orange)}
.mainnav a{position:absolute;top:0;line-height:47px;color:#fff;text-decoration:none;font-family:"Raleway",sans-serif;font-weight:700;font-size:14px;letter-spacing:.5px}
.nav-cta{position:absolute;left:670px;top:0;width:245px;height:47px;background:var(--orange-dark);clip-path:polygon(14px 0,100% 0,calc(100% - 14px) 100%,0 100%);color:#fff;font-family:"Raleway",sans-serif;font-weight:700;font-size:14px;line-height:47px;text-align:center;letter-spacing:.5px}

/* hero */
.hero{height:453px}
.hero-photo{position:absolute;inset:0;background:linear-gradient(180deg,#7fb2dc 0%,#a9cbe6 28%,#d9e1e6 45%,#9fa9a7 58%,#6f8a5a 68%,#5d7f8c 80%,#4c6d7c 100%)}
.hero-kicker{top:112px;width:1200px;text-align:center;color:#fff;font-family:"Raleway",sans-serif;font-weight:700;font-size:15px;letter-spacing:1px}
.hero-title{top:140px;width:1200px;text-align:center;color:#fff;font-family:"Raleway",sans-serif;font-weight:800;font-size:62px;line-height:66px;letter-spacing:1px;text-shadow:0 2px 6px rgba(0,0,0,.25)}
.hero .btn{left:510px;top:290px;width:185px;height:42px}

/* featured */
.featured{height:923px;background:#fff}
.featured h2.section-title{top:52px}
.featured .divider{top:100px}
.featured .lead{top:125px;left:300px;width:600px}
.card{position:absolute;width:288px;height:310px;background:#f7f7f7}
.card-photo{position:absolute;left:0;top:0;width:288px;height:186px}
.card-bar{position:absolute;left:0;top:186px;width:288px;height:32px;background:var(--teal);color:#fff;font-family:"Raleway",sans-serif;font-weight:700;font-size:15px;line-height:32px;padding-left:16px}
.card-text{position:absolute;left:16px;top:230px;width:256px;font-size:11px;line-height:14px;color:#777;text-align:justify}
.price{position:absolute;left:8px;top:8px;background:var(--orange);color:#fff;font-weight:700;font-size:13px;padding:4px 10px}
.card-overlay{position:absolute;left:0;top:0;width:288px;height:186px;background:rgba(0,0,0,.35)}
.card .btn{left:74px;top:74px;width:140px;height:42px;font-size:13px}

/* welcome */
.welcome{height:417px;background:var(--soft)}
.welcome-curve{position:absolute;left:0;bottom:0;width:1200px;height:60px}
.welcome-title{left:132px;top:59px;font-family:"Raleway",sans-serif;font-weight:700;font-size:30px;line-height:38px;color:var(--ink)}
.welcome .divider{left:122px;top:141px}
.welcome-text{left:132px;top:175px;width:460px;font-size:13px;line-height:19px;color:#555}
.welcome .btn{left:132px;top:283px;width:190px;height:44px;font-size:13px}
.video{left:623px;top:64px;width:443px;height:263px;background:linear-gradient(180deg,#6ea7d8 0%,#b9d08d 40%,#e0a93a 55%,#5a5f63 68%,#6f9a3c 85%,#4e7f2c 100%);box-shadow:0 4px 12px rgba(0,0,0,.25)}
.video-label{position:absolute;left:28px;bottom:28px;display:flex;align-items:center;gap:10px;color:#fff;font-family:"Raleway",sans-serif;font-weight:700;font-size:13px}

/* why */
.why{height:355px;background:#fff}
.why h2.section-title{top:32px}
.why .divider{top:80px}
.feature{position:absolute;top:150px;width:260px;text-align:center}
.feature svg{position:absolute;left:112px;top:-30px;width:36px;height:36px}
.feature h3{margin-top:18px;font-family:"Raleway",sans-serif;font-weight:600;font-size:14px;color:var(--ink);letter-spacing:.3px}
.feature p{margin-top:14px;font-size:11.5px;line-height:16px;color:#666}

/* reservation */
.reserve{height:683px;background:#f7f7f7}
.reserve h2.section-title{top:72px}
.reserve .divider{top:120px}
.reserve .lead{top:148px;left:290px;width:620px}
.field{position:absolute;height:40px;background:#fff;border:1px solid var(--line);font-family:"Noto Serif",serif;font-size:13px;color:#aaa;padding-left:20px;line-height:38px}
.pay-label{left:132px;top:398px;font-family:"Noto Serif",serif;font-weight:700;font-size:15px;color:var(--ink)}
.reserve .btn{left:132px;top:563px;width:150px;height:40px}
.calendar{left:597px;top:207px;width:469px;height:398px;background:#fff;box-shadow:0 2px 10px rgba(0,0,0,.12)}
.cal-title{position:absolute;left:45px;top:24px;font-family:"Raleway",sans-serif;font-weight:600;font-size:40px;color:var(--teal)}
.cal-rule{position:absolute;left:45px;top:82px;width:380px;height:1px;background:var(--line)}
.cal-head{position:absolute;left:45px;top:95px;display:grid;grid-template-columns:repeat(7,54px);font-weight:700;font-size:12px;color:var(--ink);text-align:center}
.cal-grid{position:absolute;left:45px;top:122px;display:grid;grid-template-columns:repeat(7,50px);grid-auto-rows:44px;gap:4px}
.day{border:1px solid var(--line);font-size:9px;position:relative;background:#fff}
.day.blank{border:none;background:transparent}
.day b{position:absolute;right:4px;bottom:4px;font-weight:600;color:#444}
.day i{position:absolute;left:3px;top:4px;font-style:normal;font-size:6.5px;font-weight:700}
.day .open{color:#e0574a}
.day .booked{color:var(--teal)}

/* footer */
.site-footer{height:342px;background:var(--footer);color:#ddd}
.foot-brand{left:132px;top:44px;display:flex;align-items:center;gap:12px}
.foot-about{left:132px;top:138px;width:300px;font-size:13px;line-height:17px;color:#e8e8e8}
.foot-title{font-family:"Raleway",sans-serif;font-weight:600;font-size:18px;color:var(--orange);letter-spacing:.5px}
.foot-links{display:grid;grid-template-columns:160px 120px;row-gap:15px;margin-top:22px;font-size:13px;color:#eee}
.recent{display:flex;gap:12px;margin-top:16px}
.recent-thumb{width:70px;height:40px;background:linear-gradient(180deg,#8fb0c8,#b8a58a 60%,#6b7d55)}
.recent strong{display:block;color:var(--orange);font-size:13px;font-weight:600}
.recent span{display:block;font-size:11px;line-height:14px;color:#ddd;width:290px}
.foot-bottom{left:132px;top:310px;width:938px;display:flex;justify-content:space-between;font-size:10px;color:#ccc}
</style>
</head>
<body>

<header class="topbar">
  <div class="abs brand"><span class="brand-mark"></span><span class="brand-name">THE ORCHARD</span></div>
  <div class="abs contact-item" style="left:700px">
    <svg viewBox="0 0 38 38"><circle cx="19" cy="19" r="17" fill="none" stroke="#2bbcaa" stroke-width="1.5"/><path d="M19 10a6 6 0 0 0-6 6c0 5 6 12 6 12s6-7 6-12a6 6 0 0 0-6-6z" fill="#2bbcaa"/><circle cx="19" cy="16" r="2.2" fill="#fff"/></svg>
    <div><small>48 Harbor Lane</small><strong>Springfield, IL 62704</strong></div>
  </div>
  <div class="abs contact-item" style="left:910px">
    <svg viewBox="0 0 38 38"><circle cx="19" cy="19" r="17" fill="none" stroke="#2bbcaa" stroke-width="1.5"/><path d="M13 11l4 0 2 5-2.5 1.5a11 11 0 0 0 5 5L23 20l5 2v4c-9 1-16-6-15-15z" fill="#2bbcaa"/></svg>
    <div><small>Call us now</small><strong>555 - 010 - 2288</strong></div>
  </div>
</header>

<nav class="mainnav">
  <a style="left:130px">HOME</a>
  <a style="left:218px">AVAILABILITY</a>
  <a style="left:360px">GALLERY</a>
  <a style="left:470px">BLOGS</a>
  <a style="left:565px">CONTACT</a>
  <div class="nav-cta">MAKE A RESERVATION</div>
</nav>

<section class="hero">
  <div class="hero-photo" role="img" aria-label="Waterfront luxury bungalows with white facades reflected in a canal under a blue sky"></div>
  <div class="abs hero-kicker">INDOOR &amp; OUTDOOR</div>
  <h1 class="abs hero-title">ENJOY A LUXURY<br>EXPERIENCE</h1>
  <div class="btn">Make a Reservation</div>
</section>

<section class="featured">
  <h2 class="section-title">FEATURED PROPERTY</h2>
  <div class="divider center-divider"></div>
  <p class="lead">Lorem ipsum dolor sit amet, consectetur adipisicing elit. Earum totam dolores voluptatem porro tempore temporibus dulmus</p>

  <article class="card" style="left:132px;top:202px">
    <div class="card-photo" role="img" aria-label="Villa garden with trees at dusk" style="background:linear-gradient(180deg,#5d6b4f,#2f3a2a 60%,#3d4a2f)"></div>
    <div class="card-overlay"></div>
    <div class="btn">View Details</div>
    <div class="card-bar">NEW SUPERB VILLA</div>
    <p class="card-text">Lorem ipsum dolor sit amet, lacus integer non. Sit cras augue et quis lacus, pretium arcu, adipiscing dis, pellentesque quis. Potenti cum aliquam donec faucibus, nunc nulla feugiat duis viverra vestibulum, cum felis quam, arcu nibh aenean</p>
  </article>
  <article class="card" style="left:460px;top:202px">
    <div class="card-photo" role="img" aria-label="Outdoor swimming pool with palm trees" style="background:linear-gradient(180deg,#9cc3e4,#6f9a5a 45%,#3fa6c9 70%,#b07a4e)"></div>
    <div class="price">$ 1200.33</div>
    <div class="card-bar">NEW SUPERB VILLA</div>
    <p class="card-text">Lorem ipsum dolor sit amet, lacus integer non. Sit cras augue et quis lacus, pretium arcu, adipiscing dis, pellentesque quis. Potenti cum aliquam donec faucibus, nunc nulla feugiat duis viverra vestibulum, cum felis quam, arcu nibh aenean</p>
  </article>
  <article class="card" style="left:782px;top:202px">
    <div class="card-photo" role="img" aria-label="Bright bedroom with twin beds" style="background:linear-gradient(180deg,#e8e6e0,#cfd4d8 50%,#f4f4f4 75%,#b8a894)"></div>
    <div class="price">$ 1825.64</div>
    <div class="card-bar">NEW SUPERB VILLA</div>
    <p class="card-text">Lorem ipsum dolor sit amet, lacus integer non. Sit cras augue et quis lacus, pretium arcu, adipiscing dis, pellentesque quis. Potenti cum aliquam donec faucibus, nunc nulla feugiat duis viverra vestibulum, cum felis quam, arcu nibh aenean</p>
  </article>
  <article class="card" style="left:132px;top:546px">
    <div class="card-photo" role="img" aria-label="Living room with red sofa" style="background:linear-gradient(180deg,#e6e1d8,#d8d2c6 45%,#b2332a 65%,#8a7d6c)"></div>
    <div class="price">$ 1289.33</div>
    <div class="card-bar">NEW SUPERB VILLA</div>
    <p class="card-text">Lorem ipsum dolor sit amet, lacus integer non. Sit cras augue et quis lacus, pretium arcu, adipiscing dis, pellentesque quis. Potenti cum aliquam donec faucibus, nunc nulla feugiat duis viverra vestibulum, cum felis quam, arcu nibh aenean</p>
  </article>
  <article class="card" style="left:460px;top:546px">
    <div class="card-photo" role="img" aria-label="Bungalow with covered patio and lawn" style="background:linear-gradient(180deg,#9ec5e6,#d9d2c4 40%,#6a5a48 60%,#7fa34c 80%)"></div>
    <div class="price">$ 1200.33</div>
    <div class="card-bar">NEW SUPERB VILLA</div>
    <p class="card-text">Lorem ipsum dolor sit amet, lacus integer non. Sit cras augue et quis lacus, pretium arcu, adipiscing dis, pellentesque quis. Potenti cum aliquam donec faucibus, nunc nulla feugiat duis viverra vestibulum, cum felis quam, arcu nibh aenean</p>
  </article>
  <article class="card" style="left:782px;top:546px">
    <div class="card-photo" role="img" aria-label="Brick bungalow with flowering bougainvillea" style="background:linear-gradient(135deg,#8a4a34,#a3583e 40%,#c8488a 70%,#5f7a3a)"></div>
    <div class="price">$ 1285.64</div>
    <div class="card-bar">NEW SUPERB VILLA</div>
    <p class="card-text">Lorem ipsum dolor sit amet, lacus integer non. Sit cras augue et quis lacus, pretium arcu, adipiscing dis, pellentesque quis. Potenti cum aliquam donec faucibus, nunc nulla feugiat duis viverra vestibulum, cum felis quam, arcu nibh aenean</p>
  </article>
</section>

<section class="welcome">
  <h2 class="abs welcome-title">WELCOME TO THE ORCHARD<br>BUNGALOWS</h2>
  <div class="divider"></div>
  <p class="abs welcome-text">Lorem ipsum dolor sit amet, hendrerit non laoreet, suscipit nullam nam sed platea. Imperdiet massa nunc, libero urna sollicitudin tempus sed, sit vehicula mauris ac purus sollicitudin. Lacinia sed maxime phasellus pellentesque massa, sem sit nibh consectetuer malesuada massa aenean. Sit mattis placerat, leo mauris vel mollis, ut sociis id turpis est risus varius.</p>
  <div class="btn">Make a Reservation</div>
  <div class="abs video" role="img" aria-label="Modern timber house among autumn trees, intro video preview">
    <div class="video-label"><svg width="24" height="24" viewBox="0 0 24 24"><circle cx="12" cy="12" r="11" fill="#fff"/><path d="M10 7l6 5-6 5z" fill="#444"/></svg>WATCH INTRO VIDEO</div>
  </div>
  <svg class="welcome-curve" viewBox="0 0 1200 60" preserveAspectRatio="none"><path d="M0 60 Q600 -10 1200 60 Z" fill="#fff"/></svg>
</section>

<section class="why">
  <h2 class="section-title">WHY CHOOSE US</h2>
  <div class="divider center-divider"></div>
  <div class="feature" style="left:144px">
    <svg viewBox="0 0 36 36"><circle cx="18" cy="18" r="16" fill="none" stroke="#2bbcaa" stroke-width="1.5"/><path d="M10 18l8-7 8 7h-2.5v7h-4v-5h-3v5h-4v-7z" fill="#2bbcaa"/></svg>
    <h3>AFFORDABLE RENTS</h3>
    <p>Lorem ipsum dolor sit amet, hendrerit non laoreet, suscipit nullam nam sed platea. Imperdiet massa nunc, libero urna sollicitudin tempus sed, sit vehicula mauris ac purus sollicitudin.</p>
  </div>
  <div class="feature" style="left:471px">
    <svg viewBox="0 0 36 36"><circle cx="18" cy="18" r="16" fill="none" stroke="#2bbcaa" stroke-width="1.5"/><text x="18" y="24" text-anchor="middle" font-family="Open Sans,sans-serif" font-size="17" font-weight="700" fill="#2bbcaa">$</text></svg>
    <h3>EASE OF PAYMENTS</h3>
    <p>Lorem ipsum dolor sit amet, hendrerit non laoreet, suscipit nullam nam sed platea. Imperdiet massa nunc, libero urna sollicitudin tempus sed, sit vehicula mauris ac purus sollicitudin.</p>
  </div>
  <div class="feature" style="left:800px">
    <svg viewBox="0 0 36 36"><circle cx="18" cy="18" r="16" fill="none" stroke="#2bbcaa" stroke-width="1.5"/><path d="M11 25c0-9 6-14 15-14 0 9-5 14-13 14z" fill="#2bbcaa"/><path d="M11 25l9-8" stroke="#fff" stroke-width="1.3"/></svg>
    <h3>PEACEFUL LOCATION</h3>
    <p>Lorem ipsum dolor sit amet, hendrerit non laoreet, suscipit nullam nam sed platea. Imperdiet massa nunc, libero urna sollicitudin tempus sed, sit vehicula mauris ac purus sollicitudin.</p>
  </div>
</section>

<section class="reserve">
  <h2 class="section-title">MAKE A RESERVATION</h2>
  <div class="divider center-divider"></div>
  <p class="lead">Lorem ipsum dolor sit amet, hendrerit non laoreet, suscipit nullam nam sed platea. Imperdiet massa nunc, libero urna sollicitudin temp</p>

  <div class="field" style="left:132px;top:207px;width:440px">First Name</div>
  <div class="field" style="left:132px;top:267px;width:440px">Last Name</div>
  <div class="field" style="left:132px;top:330px;width:440px">Email Address</div>
  <div class="abs pay-label">PAYMENT DETAILS</div>
  <div class="field" style="left:132px;top:423px;width:208px">Credit Card Number</div>
  <div class="field" style="left:365px;top:423px;width:207px">CCV</div>
  <div class="field" style="left:132px;top:485px;width:208px">Expiry Date: DD/MM/YY</div>
  <div class="field" style="left:365px;top:485px;width:207px">Amount Payable</div>
  <div class="btn">Reserve</div>

  <div class="abs calendar">
    <div class="cal-title">JAN / 2019</div>
    <div class="cal-rule"></div>
    <div class="cal-head"><span>S</span><span>M</span><span>T</span><span>W</span><span>T</span><span>F</span><span>S</span></div>
    <div class="cal-grid">
      <div class="day blank"></div><div class="day blank"></div>
      <div class="day"><i class="open">AVAILABLE</i><b>1</b></div>
      <div class="day"><i class="open">AVAILABLE</i><b>2</b></div>
      <div class="day"><b>3</b></div>
      <div class="day"><b>4</b></div>
      <div class="day"><b>5</b></div>
      <div class="day"><b>6</b></div>
      <div class="day"><i class="booked">BOOKED</i><b>7</b></div>
      <div class="day"><b>8</b></div>
      <div class="day"><i class="booked">BOOKED</i><b>9</b></div>
      <div class="day"><i class="booked">BOOKED</i><b>10</b></div>
      <div class="day"><b>11</b></div>
      <div class="day"><i class="booked">BOOKED</i><b>12</b></div>
      <div class="day"><i class="open">AVAILABLE</i><b>13</b></div>
      <div class="day"><b>14</b></div>
      <div class="day"><i class="booked">BOOKED</i><b>15</b></div>
      <div class="day"><i class="open">AVAILABLE</i><b>16</b></div>
      <div class="day"><i class="open">AVAILABLE</i><b>17</b></div>
      <div class="day"><b>18</b></div>
      <div class="day"><i class="open">AVAILABLE</i><b>19</b></div>
      <div class="day"><b>20</b></div>
      <div class="day"><i class="open">AVAILABLE</i><b>21</b></div>
      <div class="day"><i class="open">AVAILABLE</i><b>22</b></div>
      <div class="day"><b>23</b></div>
      <div class="day"><i class="open">AVAILABLE</i><b>24</b></div>
      <div class="day"><i class="booked">BOOKED</i><b>25</b></div>
      <div class="day"><i class="booked">BOOKED</i><b>26</b></div>
      <div class="day"><b>27</b></div>
      <div class="day"><i class="open">AVAILABLE</i><b>28</b></div>
      <div class="day"><b>29</b></div>
      <div class="day"><i class="booked">BOOKED</i><b>30</b></div>
      <div class="day"><b>31</b></div>
    </div>
  </div>
</section>

<footer class="site-footer">
  <div class="abs foot-brand"><span class="brand-mark"></span><span class="brand-name">THE ORCHARD</span></div>
  <p class="abs foot-about">You have questions regarding our services? Contact us, we will be happy to help you out! Lorem ipsum dolor sit amet, ipsum dolor sociosqu, condimentum consectetuer est nec dui, vitae hac amet vitae vitae, eget pulvinar maecenas eu ante morbi, eleifend augue sagittis ipsum amet ante praesent</p>
  <div class="abs" style="left:445px;top:100px">
    <div class="foot-title">INQUIRES</div>
    <div class="foot-links">
      <span>Accommodation</span><span>Offes</span>
      <span>About</span><span>Residences</span>
      <span>Services &amp; Amenities</span><span>Careers</span>
      <span>Destination</span><span>Contact us</span>
    </div>
  </div>
  <div class="abs" style="left:708px;top:100px">
    <div class="foot-title">RECENT PROPERTIES</div>
    <div class="recent"><div class="recent-thumb" role="img" aria-label="Property exterior thumbnail"></div><div><strong>12 Willow Court</strong><span>Lorem ipsum dolor sit amet, ipsum dolor sociosqu, condimentum consectetuer est nec dui</span></div></div>
    <div class="recent"><div class="recent-thumb" role="img" aria-label="Property exterior thumbnail"></div><div><strong>88 Maple Avenue</strong><span>Lorem ipsum dolor sit amet, ipsum dolor sociosqu, condimentum consectetuer est nec dui</span></div></div>
  </div>
  <div class="abs foot-bottom"><span>© Copyright . All Right Reserved</span><span>Privacy Policy &nbsp;&nbsp; | &nbsp;&nbsp; Terms &amp; Conditions</span></div>
</footer>

</body>
</html>
```